Wedding Day Custom Wine Label - Tasmanian (Tamar Valley) wine

I am looking for a custom design that will be put on a wine label to commemorate a very good friend's wedding day.

We will need to be able to take the design and print it on to sticker labels that we can put on to wine bottles.

The bride and groom have asked for a simplistic label design (see example image attached). We need two labels. One for "Pinot Noir" wine and the other for "Chardonnay" wine. We would like the label to say:

The Hartwell's
Pinot Noir
2023
Tamar Valley

and for for the other wine variety:

The Hartwell's
Chardonnay
2023
Tamar Valley

smaller text below to say:

13.5% ALC/VOL 750ML
MEGAN & LIAM - 31.10.2024

I am happy to consider other variations - the bride & groom would prefer something minimalistic. Elegant and classy.

Target Market(s)

the bride & groom

Requirements
Must have
• Wedding date (31.10.2024). Wine type (Pinot Noir or Chardonnay).
Should not have
• images not essential

```html
<!DOCTYPE html>
<html lang="en">
<head>
<meta charset="utf-8">
<title>The Hartwell's Wedding Wine Labels</title>
<link href="https://fonts.googleapis.com/css2?family=Special+Elite&family=Smokum&family=Rye&family=Sancreek&family=Ewert&family=Stint+Ultra+Condensed&family=Bungee+Hairline&family=Oswald:wght@400;500&display=swap" rel="stylesheet">
<style>
  :root {
    --backdrop: #000000;
    --label: #cdcbc6;
    --ink: #0b0b0b;
  }
  html, body {
    margin: 0;
    padding: 0;
    width: 1200px;
    height: 1200px;
    overflow: hidden;
    background: var(--backdrop);
  }
  .sheet {
    position: relative;
    width: 1200px;
    height: 1200px;
  }
  .label {
    position: absolute;
    top: 267px;
    width: 511px;
    height: 705px;
    background: var(--label);
    color: var(--ink);
    font-family: "Oswald", "Arial Narrow", sans-serif;
    text-transform: uppercase;
  }
  .label--pinot { left: 68px; }
  .label--chardonnay { left: 625px; }
  .label__frame {
    position: absolute;
    left: 20px;
    top: 28px;
    right: 24px;
    bottom: 28px;
    border: 1.5px solid var(--ink);
    border-radius: 2px;
  }
  .label__text {
    position: absolute;
    left: 0;
    right: 0;
    text-align: center;
    margin: 0;
    line-height: 1;
    font-weight: 500;
  }
  .label__house { top: 88px; font-size: 43px; letter-spacing: 1px; }
  .label__variety { top: 196px; font-size: 62px; letter-spacing: 1px; }
  .label__region { top: 298px; font-size: 62px; letter-spacing: 1px; }
  .label__vintage { top: 374px; font-size: 62px; }
  .label__couple { top: 476px; font-size: 30px; letter-spacing: 1.5px; }
  .label__date { top: 514px; font-size: 28px; }
  .label__abv { top: 578px; font-size: 26px; }
  .label__volume { top: 618px; font-size: 26px; }
</style>
</head>
<body>
<main class="sheet">
  <section class="label label--pinot">
    <div class="label__frame"></div>
    <p class="label__text label__house">The Hartwell's</p>
    <p class="label__text label__variety">Pinot Noir</p>
    <p class="label__text label__region">Tamar Valley</p>
    <p class="label__text label__vintage">2023</p>
    <p class="label__text label__couple">Megan &amp; Liam</p>
    <p class="label__text label__date">31.10.2024</p>
    <p class="label__text label__abv">13.5% ALC/VOL</p>
    <p class="label__text label__volume">750ML</p>
  </section>
  <section class="label label--chardonnay">
    <div class="label__frame"></div>
    <p class="label__text label__house">The Hartwell's</p>
    <p class="label__text label__variety">Chardonnay</p>
    <p class="label__text label__region">Tamar Valley</p>
    <p class="label__text label__vintage">2023</p>
    <p class="label__text label__couple">Megan &amp; Liam</p>
    <p class="label__text label__date">31.10.2024</p>
    <p class="label__text label__abv">13.5% ALC/VOL</p>
    <p class="label__text label__volume">750ML</p>
  </section>
</main>
</body>
</html>
```